Property Development Business Cards

I need a business card design for Blue Harbour Developments Pty Ltd. We are a property development company in Australia and our name defines the five values that we adhere to, being Profitable, Partnerships, Quality Developments, Eco Friendly and Enduring Design.

I have attached the current logo that I use, it is just five yellow circles connected to a single cricle in the middle.

Target Market(s)

Our Target audience is real estate agents, owners of properties, builders and other trades

Industry/Entity Type

Business

Requirements
Must have
• Want to have two sides to the card, one with details and one to just highlight the company

```html
<!DOCTYPE html>
<html lang="en">
<head>
<meta charset="utf-8">
<title>Blue Harbour Developments – Business Cards</title>
<link rel="stylesheet" href="https://fonts.googleapis.com/css2?family=Arimo:wght@400;700&family=Great+Vibes&display=swap">
<style>
  :root {
    --page: #ffffff;
    --orange: #f5b540;
    --band-pale: #f8d49a;
    --band-yellow: #fff033;
    --card-white: #ffffff;
    --ink-blue: #2a2ad8;
    --ink-black: #111111;
    --card-shadow: rgba(0,0,0,0.28);
  }
  html, body {
    margin: 0;
    width: 1200px;
    height: 900px;
    overflow: hidden;
    background: var(--page);
    font-family: "Arimo", Arial, sans-serif;
  }
  .canvas {
    position: relative;
    width: 1200px;
    height: 900px;
  }
  .card {
    position: absolute;
    top: 295px;
    width: 540px;
    height: 310px;
    overflow: hidden;
    box-shadow: 0 10px 24px var(--card-shadow);
    background: var(--orange);
  }
  .card--front { left: 40px; }
  .card--back { left: 620px; }
  .card__art {
    position: absolute;
    inset: 0;
    width: 100%;
    height: 100%;
  }
  .company-name {
    position: absolute;
    top: 42px;
    left: 215px;
    width: 310px;
    margin: 0;
    text-align: center;
    color: var(--ink-blue);
    font-weight: 700;
    font-size: 27px;
    line-height: 1.15;
  }
  .person {
    position: absolute;
    top: 140px;
    left: 262px;
  }
  .person__name {
    display: block;
    font-family: "Great Vibes", cursive;
    color: var(--ink-blue);
    font-size: 24px;
    line-height: 1;
    padding-left: 4px;
  }
  .person__role {
    display: block;
    margin-top: 4px;
    font-size: 12px;
    letter-spacing: 4px;
    color: var(--ink-black);
  }
  .address {
    position: absolute;
    top: 152px;
    left: 420px;
    font-size: 11px;
    line-height: 1.3;
    color: var(--ink-black);
    font-style: normal;
  }
  .website {
    position: absolute;
    color: var(--ink-blue);
    font-weight: 700;
    text-decoration: none;
  }
  .card--front .website {
    bottom: 26px;
    left: 250px;
    font-size: 12px;
    font-weight: 400;
  }
  .card--back .website {
    bottom: 30px;
    right: 24px;
    font-size: 17px;
  }
  .brand-mark {
    position: absolute;
    display: flex;
    align-items: center;
    gap: 8px;
    font-weight: 700;
    white-space: nowrap;
  }
  .brand-mark__dot {
    border-radius: 50%;
    flex: none;
  }
  .card--front .brand-mark {
    top: 178px;
    left: 16px;
    color: var(--card-white);
    font-size: 17px;
  }
  .card--front .brand-mark__dot {
    width: 22px;
    height: 22px;
    background: var(--card-white);
  }
  .card--back .brand-mark {
    top: 118px;
    left: 90px;
    color: var(--ink-blue);
    font-size: 30px;
  }
  .card--back .brand-mark__dot {
    width: 40px;
    height: 40px;
    background: var(--orange);
  }
</style>
</head>
<body>
<main class="canvas">

  <section class="card card--front" aria-label="Card front with contact details">
    <svg class="card__art" viewBox="0 0 540 310" aria-hidden="true">
      <rect width="540" height="310" fill="var(--orange)"/>
      <ellipse cx="600" cy="60" rx="448" ry="352" fill="var(--band-pale)"/>
      <ellipse cx="600" cy="60" rx="434" ry="341" fill="var(--band-yellow)"/>
      <ellipse cx="600" cy="60" rx="420" ry="330" fill="var(--card-white)"/>
    </svg>
    <div class="brand-mark">
      <span class="brand-mark__dot"></span>
      <span>Blue Harbour</span>
    </div>
    <h1 class="company-name">Blue Harbour Developments<br>Pty Ltd</h1>
    <p class="person">
      <span class="person__name">Daniel</span>
      <span class="person__role">Director</span>
    </p>
    <address class="address">PO Box 518<br>Kingsford, ACT 2915</address>
    <a class="website" href="#">www.blueharbourdevelopments.com.au</a>
  </section>

  <section class="card card--back" aria-label="Card back highlighting the company">
    <svg class="card__art" viewBox="0 0 540 310" aria-hidden="true">
      <rect width="540" height="310" fill="var(--orange)"/>
      <ellipse cx="160" cy="140" rx="356" ry="282" fill="var(--band-pale)"/>
      <ellipse cx="160" cy="140" rx="343" ry="271" fill="var(--band-yellow)"/>
      <ellipse cx="160" cy="140" rx="330" ry="260" fill="var(--card-white)"/>
    </svg>
    <div class="brand-mark">
      <span class="brand-mark__dot"></span>
      <span>Blue Harbour</span>
    </div>
    <a class="website" href="#">www.blueharbourdevelopments.com.au</a>
  </section>

</main>
</body>
</html>
```